Legal Industry Crowdsourcing Website

BriefHarbor.com will be a new crowdsourcing website. The audiences are law students and legal professionals, and individual citizens, predominantly those working for or running small businesses. The objective is to enable them to get cheap or free legal advice and opinions.

Think of it like ArtMingle.com but for lawyers. NB: BriefHarbor.com is NOT a law firm.

Do not include pictures of gavels (the wooden hammers). They are not used in the courts of England & Wales.
Updates

Target Market(s)

Legal industry, small business owners

Industry/Entity Type

Lawyer

Number of Pages Required

1 page

Requirements
Must have
• It must show the information presented in the Powerpoint file attached to the brief
• Must also show how the page appears on mobile devices.
Should not have
• Should not have:
• Pictures of gavels (the wooden hammers). They are not used in the courts of England & Wales.
• A vertical ever-scrolling design

```html
<!DOCTYPE html>
<html lang="en">
<head>
<meta charset="utf-8">
<title>BriefHarbor – Legal opinions from many advisors</title>
<link href="https://fonts.googleapis.com/css2?family=Cinzel:wght@400;600&family=Open+Sans:wght@400;600&display=swap" rel="stylesheet">
<style>
:root{
  --gold:#c6952b;
  --gold-dark:#a97a18;
  --gold-glass:rgba(201,152,38,.9);
  --ink:#1c1c1c;
  --text:#333;
  --muted:#6d6d6d;
  --line:#dcdcdc;
  --bar:#e8e8e8;
  --card:#efefef;
  --footer:#161616;
  --white:#fff;
}
*{box-sizing:border-box;margin:0;padding:0}
html,body{width:1200px;height:2206px;overflow:hidden}
body{position:relative;background:var(--white);font-family:"Open Sans",Arial,sans-serif;color:var(--text)}
h1,h2,h3{font-weight:400}
.abs{position:absolute}

/* utility bar */
.utility-bar{left:0;top:0;width:1200px;height:44px;background:var(--bar)}
.utility-link{top:15px;font-size:11px;color:#444;display:flex;align-items:center;gap:4px}
.utility-link svg{width:10px;height:10px;fill:var(--gold)}

/* header */
.site-header{left:0;top:44px;width:1200px;height:93px;background:var(--white)}
.brand{left:112px;top:28px;display:flex;align-items:center;gap:8px;font-family:"Cinzel",Georgia,serif;font-size:15px;color:#3a2f1a;font-weight:400}
.brand-dot{width:26px;height:26px;border-radius:50%;background:var(--gold)}
.nav-item{top:41px;font-size:11px;color:#555;letter-spacing:.3px}
.nav-item.active{top:30px;left:632px;width:86px;height:38px;border:1.5px solid var(--gold);display:flex;align-items:center;justify-content:center;font-weight:600;color:#222}

/* hero */
.hero{left:0;top:137px;width:1200px;height:559px;background:linear-gradient(90deg,#1d2430 0%,#2a2f38 38%,#5a2a24 55%,#7d2b2d 70%,#3b3436 85%,#6b2a2c 100%)}
.hero-arrow{top:265px;width:22px;height:30px}
.hero-arrow path{fill:none;stroke:var(--white);stroke-width:4}
.hero-panel{left:140px;top:285px;width:922px;height:221px;background:var(--gold-glass)}
.hero-title{position:absolute;left:0;top:28px;width:100%;text-align:center;font-family:"Cinzel",Georgia,serif;font-size:31px;line-height:42px;color:#111;letter-spacing:.5px;font-weight:400}
.btn-dark{position:absolute;background:#111;color:var(--white);font-size:14px;display:flex;align-items:center;justify-content:center;gap:6px;border-radius:2px;letter-spacing:.2px}
.btn-dark svg{width:13px;height:13px}

/* sections */
.section-title{left:0;width:1200px;text-align:center;font-family:"Cinzel",Georgia,serif;font-size:27px;color:#111;letter-spacing:.5px;font-weight:400}

/* issue grid */
.issue{width:310px;height:112px;border-bottom:1px solid var(--line);display:flex;align-items:center;gap:20px}
.issue-icon{flex:none;width:64px;height:64px;border-radius:50%;background:radial-gradient(circle at 40% 35%,#d9a63a,var(--gold-dark));box-shadow:0 2px 3px rgba(0,0,0,.25);display:flex;align-items:center;justify-content:center}
.issue-icon svg{width:30px;height:30px;fill:#161616}
.issue-text{font-size:12px;line-height:20px;color:#555;letter-spacing:-.1px;width:226px}

/* advisor cards */
.advisor-card{top:1209px;width:227px;height:545px;background:var(--card)}
.advisor-photo{position:absolute;left:3px;top:3px;width:221px;height:171px}
.advisor-facts{position:absolute;left:24px;top:186px;width:180px;list-style:none}
.advisor-facts li{border-bottom:1px solid var(--line);font-size:11px;color:#222;padding:10px 0 10px}
.advisor-facts li .value{color:var(--muted)}
.advisor-facts li.stacked .value{display:block;margin-top:4px}
.advisor-facts li:last-child{border-bottom:none}
.advisor-facts li .stars{color:var(--gold);letter-spacing:1px;font-size:12px}
.advisor-card .btn-dark{left:19px;top:460px;width:187px;height:53px;font-size:13px}

/* footer */
.site-footer{left:0;top:1784px;width:1200px;height:353px;background:linear-gradient(#1a1a1a,#0e0e0e)}
.footer-heading{top:45px;font-family:"Cinzel",Georgia,serif;font-size:16px;color:#eee;letter-spacing:.5px;font-weight:400}
.footer-list{top:80px;list-style:none}
.footer-list li{font-size:11px;color:#cfcfcf;line-height:14px;margin-bottom:20.3px}
.footer-list li::before{content:"» ";color:var(--gold)}
.footer-list.social li::before{content:""}
.footer-list.social li{display:flex;align-items:center;gap:5px}
.social-dot{width:9px;height:9px;border-radius:50%;background:var(--gold)}
.footer-rule{top:40px;width:1px;height:265px;background:#333}
.copyright-bar{left:0;top:2137px;width:1200px;height:69px;background:var(--gold);font-size:11px;color:#222;display:flex;align-items:center;justify-content:center}
</style>
</head>
<body>

<div class="abs utility-bar">
  <div class="abs utility-link" style="left:890px"><svg viewBox="0 0 10 10"><circle cx="5" cy="3" r="2.5"/><path d="M0 10c0-3 2.5-4.5 5-4.5S10 7 10 10z"/></svg>MY ACCOUNT</div>
  <div class="abs utility-link" style="left:1002px"><svg viewBox="0 0 10 10"><path d="M1 0h6l2 2v8H1zM2.5 4h5v1h-5zM2.5 6h5v1h-5z"/></svg>POST A BRIEF</div>
</div>

<header class="abs site-header">
  <div class="abs brand"><span class="brand-dot"></span>BriefHarbor</div>
  <div class="abs nav-item active">SECTORS</div>
  <div class="abs nav-item" style="left:743px">LEGAL ADVISORS</div>
  <div class="abs nav-item" style="left:878px">BROWSE BRIEFS</div>
  <div class="abs nav-item" style="left:1007px">HOW IT WORKS</div>
</header>

<section class="abs hero" role="img" aria-label="Photo of a lawyer in a dark suit with folded arms in front of shelves of red and navy law books">
  <svg class="abs hero-arrow" style="left:28px" viewBox="0 0 22 30"><path d="M17 3 5 15l12 12"/></svg>
  <svg class="abs hero-arrow" style="left:1152px" viewBox="0 0 22 30"><path d="M5 3l12 12L5 27"/></svg>
  <div class="abs hero-panel">
    <h1 class="hero-title">Get numerous legal opinions on your case,<br>and select your most preferred legal advisor</h1>
    <div class="btn-dark" style="left:242px;top:125px;width:202px;height:56px">GET STARTED NOW <svg viewBox="0 0 14 14"><circle cx="7" cy="7" r="7" fill="#fff"/><path d="M5.5 3.5 9 7l-3.5 3.5" stroke="#111" stroke-width="2" fill="none"/></svg></div>
    <div class="btn-dark" style="left:456px;top:125px;width:222px;height:56px">SEE HOW IT WORKS? <svg viewBox="0 0 14 14"><circle cx="7" cy="7" r="7" fill="#fff"/><path d="M5.5 3.5 9 7l-3.5 3.5" stroke="#111" stroke-width="2" fill="none"/></svg></div>
  </div>
</section>

<h2 class="abs section-title" style="top:740px">What does your issue relate to?</h2>

<div class="abs issue" style="left:110px;top:780px"><div class="issue-icon"><svg viewBox="0 0 30 30"><path d="M7 4h13l4 4v18H7zM10 10h10v2H10zM10 14h10v2H10zM10 18h7v2h-7z"/></svg></div><p class="issue-text">Purchase and Supply of goods and/or services</p></div>
<div class="abs issue" style="left:444px;top:780px"><div class="issue-icon"><svg viewBox="0 0 30 30"><path d="M5 4h12v16H5zM11 9h12l3 3v15H11zM14 15h9v2h-9zM14 19h9v2h-9z"/></svg></div><p class="issue-text">Someone copying my work, ideas, identity, trade marks</p></div>
<div class="abs issue" style="left:778px;top:780px"><div class="issue-icon"><svg viewBox="0 0 30 30"><path d="M5 5h15v20H5zM8 9h9v2H8zM8 13h9v2H8zM8 17h6v2H8zM24 8l3 3-10 10-4 1 1-4z"/></svg></div><p class="issue-text">Agreements or contracts</p></div>

<div class="abs issue" style="left:110px;top:892px"><div class="issue-icon"><svg viewBox="0 0 30 30"><path d="M2 12l6-4 5 2 4-2 6 1 5 4-3 2-5-3-5 3 8 5-3 3-9-5-4 1z"/></svg></div><p class="issue-text">The relationship between employer and employee(s)</p></div>
<div class="abs issue" style="left:444px;top:892px"><div class="issue-icon"><svg viewBox="0 0 30 30"><circle cx="15" cy="8" r="5"/><path d="M6 27c0-7 4-11 9-11s9 4 9 11zM12 19h6v5h-6z"/></svg></div><p class="issue-text">Injury to person, property or reputation</p></div>
<div class="abs issue" style="left:778px;top:892px"><div class="issue-icon"><svg viewBox="0 0 30 30"><path d="M11 2h4l1 3 3 1 2-2 3 3-2 2 1 3 3 1v4l-3 1-1 3 2 2-3 3-2-2-3 1-1 3h-4l-1-3-3-1-2 2-3-3 2-2-1-3-3-1v-4l3-1 1-3-2-2 3-3 2 2 3-1zM13 10a4 4 0 1 0 .1 0z"/></svg></div><p class="issue-text">The duties of a government agency or department</p></div>

<div class="abs issue" style="left:110px;top:1002px"><div class="issue-icon"><svg viewBox="0 0 30 30"><path d="M15 4 2 15h4v11h7v-7h4v7h7V15h4z"/></svg></div><p class="issue-text">Problems with property, land, business premises, apartments, flats, house</p></div>
<div class="abs issue" style="left:444px;top:1002px"><div class="issue-icon"><svg viewBox="0 0 30 30"><path d="M13 2h4l1 4 3 1 3-2 3 3-2 3 1 3 4 1v4l-4 1-1 3 2 3-3 3-3-2-3 1-1 4h-4l-1-4-3-1-3 2-3-3 2-3-1-3-4-1v-4l4-1 1-3-2-3 3-3 3 2 3-1zM15 9a6 6 0 1 0 .1 0zM15 12a3 3 0 1 1-.1 0z" fill-rule="evenodd"/></svg></div><p class="issue-text">The content of a will, the operation of trusts, and/or the behaviour of trustees</p></div>
<div class="abs issue" style="left:778px;top:1002px"><div class="issue-icon"><svg viewBox="0 0 30 30"><path d="M5 7h20v3H5zM5 14h20v3H5zM5 21h20v3H5z"/></svg></div><p class="issue-text">Other Issue</p></div>

<h2 class="abs section-title" style="top:1152px">Legal Advisors</h2>

<article class="abs advisor-card" style="left:110px">
  <div class="advisor-photo" role="img" aria-label="Portrait photo of the advisor" style="background:linear-gradient(135deg,#b9a648,#7d7a3a 60%,#2d3236)"></div>
  <ul class="advisor-facts">
    <li>Advisor : <span class="value">Owen Castell</span></li>
    <li>Occupation : <span class="value">Barrister</span></li>
    <li class="stacked">BriefHarbor Level : <span class="value">Barrister 1 year call</span></li>
    <li>Sector : <span class="value">Commercial</span></li>
    <li>Briefs answered : <span class="value">58</span></li>
    <li>Rating : <span class="stars">★★★★</span></li>
  </ul>
  <div class="btn-dark">ASK ME FOR ADVICE <svg viewBox="0 0 14 14"><circle cx="7" cy="7" r="7" fill="#fff"/><path d="M5.5 3.5 9 7l-3.5 3.5" stroke="#111" stroke-width="2" fill="none"/></svg></div>
</article>

<article class="abs advisor-card" style="left:360px">
  <div class="advisor-photo" role="img" aria-label="Photo of the advisor working at a desk covered with papers" style="background:linear-gradient(135deg,#c9c7c3,#9e958c 55%,#e2e2e4)"></div>
  <ul class="advisor-facts">
    <li>Advisor : <span class="value">Lydia Brannock</span></li>
    <li>Occupation : <span class="value">Student</span></li>
    <li class="stacked">BriefHarbor Level : <span class="value">Student</span></li>
    <li>Sector : <span class="value">All</span></li>
    <li>Briefs answered : <span class="value">12</span></li>
    <li>Rating : <span class="stars">★★★★★</span></li>
  </ul>
  <div class="btn-dark">ASK ME FOR ADVICE <svg viewBox="0 0 14 14"><circle cx="7" cy="7" r="7" fill="#fff"/><path d="M5.5 3.5 9 7l-3.5 3.5" stroke="#111" stroke-width="2" fill="none"/></svg></div>
</article>

<article class="abs advisor-card" style="left:610px">
  <div class="advisor-photo" role="img" aria-label="Black and white portrait photo of the advisor in a suit" style="background:linear-gradient(135deg,#3a3a3a,#9a9a9a 50%,#2a2a2a)"></div>
  <ul class="advisor-facts">
    <li>Advisor : <span class="value">Marcus Vell</span></li>
    <li>Occupation : <span class="value">Solicitor</span></li>
    <li class="stacked">BriefHarbor Level : <span class="value">Solicitor qualified for 6 years</span></li>
    <li>Sector : <span class="value">Tort / Delict</span></li>
    <li>Briefs answered : <span class="value">12</span></li>
    <li>Rating : <span class="stars">★★★</span></li>
  </ul>
  <div class="btn-dark">ASK ME FOR ADVICE <svg viewBox="0 0 14 14"><circle cx="7" cy="7" r="7" fill="#fff"/><path d="M5.5 3.5 9 7l-3.5 3.5" stroke="#111" stroke-width="2" fill="none"/></svg></div>
</article>

<article class="abs advisor-card" style="left:860px">
  <div class="advisor-photo" role="img" aria-label="Black and white portrait photo of the advisor" style="background:linear-gradient(135deg,#f2f2f2,#8a8a8a 55%,#1e1e1e)"></div>
  <ul class="advisor-facts">
    <li>Advisor : <span class="value">Riya Danvers</span></li>
    <li>Occupation : <span class="value">Solicitor</span></li>
    <li class="stacked">BriefHarbor Level : <span class="value">Solicitor qualified for 1 year</span></li>
    <li>Sector : <span class="value">Commercial, Property, Tax</span></li>
    <li>Briefs answered : <span class="value">5</span></li>
    <li>Rating : <span class="stars">★★★</span></li>
  </ul>
  <div class="btn-dark">ASK ME FOR ADVICE <svg viewBox="0 0 14 14"><circle cx="7" cy="7" r="7" fill="#fff"/><path d="M5.5 3.5 9 7l-3.5 3.5" stroke="#111" stroke-width="2" fill="none"/></svg></div>
</article>

<footer class="abs site-footer">
  <h3 class="abs footer-heading" style="left:109px">I need a?</h3>
  <ul class="abs footer-list" style="left:109px">
    <li>Commercial Law Advisor</li>
    <li>Consumer Affairs Law Advisor</li>
    <li>Contract Law Advisor</li>
    <li>Intellectual Property Law Advisor</li>
    <li>Land / Property Law Advisor</li>
    <li>Equity, Wills &amp; Trusts Law Advisor</li>
    <li>Public Law &amp; Judicial Review Advisor</li>
  </ul>
  <ul class="abs footer-list" style="left:341px">
    <li>Employment Law Advisor</li>
    <li>Defamation Law Advisor</li>
    <li>Personal Injury Law Advisor</li>
    <li>All legal advice</li>
  </ul>
  <div class="abs footer-rule" style="left:518px"></div>
  <h3 class="abs footer-heading" style="left:550px">About us</h3>
  <ul class="abs footer-list" style="left:550px">
    <li>About us</li>
    <li>How it works</li>
    <li>Contact Us</li>
    <li>Affiliate Programme?</li>
    <li>Media</li>
    <li>Help / FAQ</li>
    <li>Social Media</li>
  </ul>
  <div class="abs footer-rule" style="left:697px"></div>
  <h3 class="abs footer-heading" style="left:731px">Jurisdiction</h3>
  <ul class="abs footer-list" style="left:731px;width:190px">
    <li>England &amp; Wales</li>
    <li>United States</li>
    <li>Scotland</li>
    <li>Australia</li>
    <li>Ireland</li>
    <li>A Judicial Committee of the Privy Council</li>
    <li>Jurisdiction</li>
  </ul>
  <div class="abs footer-rule" style="left:935px"></div>
  <h3 class="abs footer-heading" style="left:963px">Follow On</h3>
  <ul class="abs footer-list social" style="left:963px">
    <li><svg width="11" height="8" viewBox="0 0 11 8"><rect width="11" height="8" fill="#c6952b"/><path d="M0 0l5.5 4.5L11 0" stroke="#161616" fill="none"/></svg>Newsletter</li>
    <li><span class="social-dot"></span>Chatterline</li>
    <li><span class="social-dot"></span>Neighbourly</li>
    <li><span class="social-dot"></span>Careerweb</li>
  </ul>
</footer>

<div class="abs copyright-bar">Copyrights @ 2015 Brief Harbor. All Right Reserved.</div>

</body>
</html>
```